Tolvin Waste Website Design

Our new start-up needs a website design. We plan to help businesses find more sustainable ways to manage their waste. Our initial website aims to gather contact data from potential business customers and comprehensive information from waste facilities and waste transporters. We have a logo design (attached) which we would like included in the website design. I have also attached a number of pages that describe what information should appear on each page as well as a web design brief file that describes the look we are after.

```html
<!DOCTYPE html>
<html lang="en">
<head>
<meta charset="utf-8">
<title>Tolvin Waste — Welcome</title>
<link rel="stylesheet" href="https://fonts.googleapis.com/css2?family=Lato:wght@400;700;900&display=swap">
<style>
  :root {
    --ink: #343434;
    --leaf: #5c9a1f;
    --leaf-light: #9ccb2c;
    --leaf-dark: #5a951f;
    --nav-grey: #8d8d8d;
    --scrim: rgba(12, 14, 12, 0.72);
    --footer-bg: #141514;
    --footer-text: #7c7c7c;
    --field-bg: #f0f0f0;
    --field-line: #cfcfcf;
    --panel: #ffffff;
  }
  * { box-sizing: border-box; margin: 0; padding: 0; }
  html, body { width: 1200px; height: 738px; overflow: hidden; }
  body { font-family: "Lato", Arial, sans-serif; background: #1c1f1b; }

  .page { position: relative; width: 1200px; height: 738px; overflow: hidden; }

  .hero-photo {
    position: absolute; inset: 0;
    background:
      radial-gradient(ellipse at 30% 30%, #6f7468 0%, transparent 55%),
      radial-gradient(ellipse at 80% 80%, #3f4a34 0%, transparent 60%),
      linear-gradient(135deg, #5d6259 0%, #3a3e36 45%, #2c3327 100%);
  }
  .hero-scrim { position: absolute; inset: 0; background: var(--scrim); }

  .site-header {
    position: absolute; top: 32px; left: 75px; right: 75px;
    display: flex; justify-content: space-between; align-items: center;
  }
  .brand { display: flex; align-items: center; gap: 10px; color: var(--nav-grey); }
  .brand-mark { width: 40px; height: 40px; border: 3px solid var(--nav-grey); border-radius: 50%; }
  .brand-name { font-size: 30px; font-weight: 700; letter-spacing: 1px; line-height: 1; }

  .main-nav { display: flex; gap: 36px; }
  .main-nav a { color: var(--nav-grey); text-decoration: none; font-size: 13px; text-transform: uppercase; }

  .audience-button {
    position: absolute; top: 390px; height: 73px; width: 300px;
    border: 2px solid rgba(150,150,150,0.7); border-radius: 8px;
    background: linear-gradient(#3e6a18, #284a10);
    color: rgba(160,170,150,0.8); font-size: 24px; font-weight: 700;
    display: flex; align-items: center; padding: 0 42px;
  }
  .audience-button.facilities { left: 162px; }
  .audience-button.transporters { left: 738px; justify-content: flex-end; }

  .site-footer {
    position: absolute; left: 0; right: 0; bottom: 0; height: 68px;
    background: rgba(16,17,16,0.85);
  }
  .copyright { position: absolute; left: 75px; top: 27px; font-size: 12px; color: var(--footer-text); }
  .footer-mark {
    position: absolute; left: 570px; top: -30px; width: 60px; height: 60px;
    border-radius: 50%; border: 4px solid #6b8f36; background: #2a2d28;
  }
  .social { position: absolute; right: 76px; top: 25px; display: flex; gap: 22px; }
  .social span { width: 18px; height: 18px; border-radius: 50%; background: #6f6f6f; display: block; }

  .signup-modal {
    position: absolute; left: 254px; top: 201px; width: 692px; height: 356px;
    background: var(--panel); border-radius: 10px; text-align: center;
  }
  .modal-close {
    position: absolute; right: 12px; top: 10px; font-size: 17px; font-weight: 700;
    color: var(--ink); background: none; border: 0; font-family: inherit;
  }
  .modal-title { margin-top: 46px; font-size: 40px; font-weight: 900; color: var(--ink); line-height: 1; }
  .modal-title .accent { color: var(--leaf); }
  .modal-lead { margin-top: 12px; font-size: 25px; font-weight: 700; color: var(--ink); }
  .modal-note { margin-top: 6px; font-size: 21px; font-weight: 700; color: var(--leaf); }

  .signup-form { position: absolute; left: 129px; top: 186px; width: 436px; }
  .email-field {
    display: block; width: 100%; height: 52px; border: 2px solid var(--field-line);
    border-radius: 10px; background: var(--field-bg); text-align: center;
    font-family: inherit; font-size: 18px; color: var(--ink);
  }
  .email-field::placeholder { color: #444; }
  .signup-button {
    display: block; width: 100%; height: 53px; margin-top: 11px; border: 0; border-radius: 10px;
    background: linear-gradient(var(--leaf-light), var(--leaf-dark));
    color: #fff; font-family: inherit; font-size: 25px; font-weight: 700;
  }
</style>
</head>
<body>
<div class="page">
  <div class="hero-photo" role="img" aria-label="Photograph of a waste sorting facility with conveyor machinery and a control panel"></div>
  <div class="hero-scrim"></div>

  <header class="site-header">
    <div class="brand"><span class="brand-mark"></span><span class="brand-name">TOLVIN WASTE</span></div>
    <nav class="main-nav">
      <a href="#">About Us</a><a href="#">What We Do</a><a href="#">Resources</a><a href="#">Contact Us</a>
    </nav>
  </header>

  <div class="audience-button facilities">Waste Facilities</div>
  <div class="audience-button transporters">Waste Transporters</div>

  <footer class="site-footer">
    <p class="copyright">Copyright © 2018 Company&nbsp; Name All rights Reserved</p>
    <span class="footer-mark"></span>
    <div class="social" aria-label="Social links"><span></span><span></span><span></span><span></span><span></span></div>
  </footer>

  <section class="signup-modal">
    <button class="modal-close">x</button>
    <h1 class="modal-title">WELCOME TO <span class="accent">TOLVIN WASTE</span></h1>
    <p class="modal-lead">We are just getting started.</p>
    <p class="modal-note">Please register your email address to receive updates from us.</p>
    <form class="signup-form">
      <input class="email-field" type="email" placeholder="Enter Email Address">
      <button class="signup-button" type="button">Sign Up</button>
    </form>
  </section>
</div>
</body>
</html>
```